REDESIGN COUPLE PAGES FOR VIMLO VIDEO ADS

PLEASE REDESIGN THIS PAGE FOR ME:
http://pageframequarry.com/kq/rudy/vimlo/pricing.html
I need it to be easy to read for the end user so the customer knows exactly what he will be getting. Make an emphasis on the subscription as the most popular item....and also the price per video format should be emphasized too.

Target Market(s)

B2B

Industry/Entity Type

Video Production

Number of Pages Required

3 page

Colors

Designer to choose colors to be used in the design.

Requirements
Must have
• PLEASE REDESIGN THIS PAGE FOR ME:
• http://pageframequarry.com/kq/rudy/vimlo/pricing.html
• I need it to be easy to read for the end user so the customer knows exactly what he will be getting. Make an emphasis on the subscription as the most popular item....and also the price per video format should be emphasized too.
Nice to have
Should not have

```html
<!DOCTYPE html>
<html lang="en">
<head>
<meta charset="utf-8">
<title>VIMLO Pricing</title>
<link href="https://fonts.googleapis.com/css2?family=Poppins:wght@400;500;600;700&family=Merriweather:wght@700;900&display=swap" rel="stylesheet">
<style>
:root{
  --navy:#141d2e;
  --ink:#0d4fa0;
  --title:#0d3a8a;
  --sky:#1aa3e0;
  --band:#e6f5fc;
  --band-soft:#f6fbfd;
  --text:#555b66;
  --bar:#c9c9c9;
  --btn-top:#2f8fe0;
  --btn-bottom:#1462b4;
  --white:#ffffff;
}
*{box-sizing:border-box;margin:0;padding:0}
html,body{width:935px;height:1200px;overflow:hidden;background:var(--white)}
body{font-family:"Poppins",sans-serif}
.page{position:relative;width:1702px;height:2184px;transform:scale(0.54935);transform-origin:0 0}

/* nav */
.topbar{position:absolute;left:0;top:0;width:1702px;height:69px;background:var(--navy)}
.brand{position:absolute;left:236px;top:14px;color:var(--white)}
.brand-name{font-size:28px;font-weight:700;letter-spacing:6px;line-height:28px}
.brand-tag{font-size:8px;font-weight:600;letter-spacing:.6px;margin-top:2px}
.nav{position:absolute;left:612px;top:25px;display:flex;gap:22px;font-size:14px;font-weight:500;color:var(--white)}
.nav .active{color:var(--sky)}
.login{position:absolute;left:1334px;top:26px;font-size:13px;color:var(--white);font-weight:500}
.signup{position:absolute;left:1389px;top:17px;width:74px;height:34px;background:linear-gradient(var(--btn-top),var(--btn-bottom));color:var(--white);font-size:13px;font-weight:500;display:flex;align-items:center;justify-content:center}

/* heading */
.headline{position:absolute;left:0;top:140px;width:1702px;text-align:center;font-family:"Merriweather",serif;font-weight:900;font-size:34px;letter-spacing:3px;color:var(--title)}
.headline em{font-style:normal;color:var(--sky)}

/* table */
.pricing{position:absolute;left:234px;top:260px;width:1226px}
.featured-glow{position:absolute;left:431px;top:-5px;width:200px;height:1555px;background:var(--white);box-shadow:0 0 18px rgba(0,0,0,.18)}
.row{position:relative;display:grid;grid-template-columns:230px 201px 200px 199px 199px 197px;align-items:center}
.row>div{height:100%;display:flex;align-items:center;justify-content:center;text-align:center;font-size:13px;color:var(--text);padding:0 8px;line-height:16px}
.row>div:first-child{justify-content:flex-start;text-align:left;padding-left:18px;color:var(--ink);font-weight:500}
.row.band{background:var(--band)}
.row>.featured{background:var(--white)}
.plans{height:75px;background:var(--band)}
.plans>div{align-items:flex-end;padding-bottom:10px;font-size:19px !important;font-weight:600;color:var(--sky) !important;line-height:21px}
.plans>div:first-child{font-weight:600}
.plans>.featured{background:transparent}
.featured-head{position:absolute;left:431px;top:-5px;width:200px;height:80px;background:linear-gradient(#0b5ea8,#1a9ee0);color:var(--white);font-size:20px;font-weight:600;text-align:center;padding-top:20px;border-radius:3px 3px 0 0}
.seller-tab{position:absolute;left:45px;bottom:0;width:110px;height:17px;background:var(--white);color:var(--sky);font-size:13px;font-weight:500;line-height:17px;clip-path:polygon(4% 0,96% 0,100% 100%,0 100%)}
.prices{height:58px;background:var(--band-soft)}
.prices>div{flex-direction:column}
.amount{font-size:21px;font-weight:600;color:var(--sky);line-height:24px}
.note{font-size:13px;font-weight:500;color:#3d4452;letter-spacing:.4px}
.body-row{height:53.75px}
.head-cell{font-weight:500}

/* selectors & totals */
.calc{position:absolute;left:464px;top:1468px;width:401px}
.calc-grid{display:grid;grid-template-columns:201px 200px}
.spin-row{height:63px;background:var(--band)}
.spin-row>div{display:flex;align-items:center;justify-content:center}
.spin-row>.featured{background:var(--white)}
.spinner{width:116px;height:34px;background:#2b7fd0;border-radius:2px;display:flex;align-items:center;justify-content:space-between;padding:0 24px;color:var(--white);font-size:16px}
.gap{height:8px}
.sum{height:54px;font-size:14px;color:#3d4452}
.sum>div{display:flex;justify-content:space-between;align-items:center;padding:0 13px}
.sum.band>div{background:var(--band)}
.sum.band>.featured,.sum>.featured{background:var(--white)}
.sum.grand{color:var(--sky);font-weight:500}
.buy-bar{height:53px;background:var(--bar);display:flex;align-items:center;justify-content:center}
.buy{width:133px;height:38px;background:linear-gradient(var(--btn-top),var(--btn-bottom));color:var(--white);font-size:16px;font-weight:600;display:flex;align-items:center;justify-content:center;border-radius:2px}
.buy-strip{position:absolute;left:865px;top:1468px;width:595px;height:53px;background:var(--bar);display:grid;grid-template-columns:199px 199px 197px}
.buy-strip>div{display:flex;align-items:center;justify-content:center;border-left:1px solid #e8e8e8}
.buy-strip>div:first-child{border-left:0}

/* footer */
.footer{position:absolute;left:0;top:1883px;width:1702px;height:301px;background:var(--navy);color:var(--white)}
.foot-brand{position:absolute;left:350px;top:76px}
.foot-brand .brand-name{font-size:44px;letter-spacing:10px;line-height:46px}
.foot-brand .brand-tag{font-size:15px;font-weight:500;letter-spacing:2.4px;margin-top:4px}
.foot-claim{position:absolute;left:350px;top:152px;font-size:17px;font-weight:600;letter-spacing:-.3px}
.foot-col{position:absolute;top:78px}
.foot-col h4{font-size:16px;font-weight:400}
.foot-col h4::after{content:"";display:block;width:24px;height:1px;background:#6d7585;margin-top:9px}
.links{list-style:none;margin-top:18px;font-size:13px;line-height:30px}
.about{font-size:15px;line-height:22px;width:330px;margin-top:20px}
.socials{display:flex;gap:13px;margin-top:28px}
.socials span{width:33px;height:33px;border-radius:50%;background:#222c40}
</style>
</head>
<body>
<div class="page">

  <header class="topbar">
    <div class="brand"><div class="brand-name">VIMLO</div><div class="brand-tag">MARKETING VIDEOS MADE FOR YOU</div></div>
    <nav class="nav"><span>Home</span><span>How It Works</span><span>Examples</span><span>FAQ</span><span>Contact Us</span><span class="active">Pricing</span><span>Calendar</span></nav>
    <span class="login">Log In</span>
    <span class="signup">Sign Up</span>
  </header>

  <h1 class="headline">NO <em>HIDDEN</em> CHARGES! CHOOSE YOUR <em>DEAL!</em></h1>

  <section class="pricing">
    <div class="featured-glow"></div>

    <div class="row plans">
      <div>FEATURES</div><div>AL A CARTE</div><div class="featured"></div><div>HOLIDAY PKG</div><div>SEASON PKG</div><div>SOCIAL MEDIA CALENDAR</div>
    </div>
    <div class="featured-head">SUBSCRIPTION<div class="seller-tab">Best Seller</div></div>

    <div class="row prices">
      <div></div>
      <div><span class="amount">$37.00</span><span class="note">(STARTS AT ONLY)</span></div>
      <div class="featured"><span class="amount">$16.00</span><span class="note">(STARTS AT ONLY)</span></div>
      <div><span class="amount">$14.00</span><span class="note">(STARTS AT ONLY)</span></div>
      <div><span class="amount">$18.00</span><span class="note">(STARTS AT ONLY)</span></div>
      <div><span class="amount">$10.00</span><span class="note">(STARTS AT ONLY)</span></div>
    </div>

    <div class="row body-row band"><div></div><div class="head-cell">VIDEO FORMAT</div><div class="featured head-cell">VIDEO FORMAT</div><div class="head-cell">VIDEO FORMAT</div><div class="head-cell">VIDEO FORMAT</div><div class="head-cell">VIDEO FORMAT</div></div>
    <div class="row body-row"><div>VIDEOS INCLUDED</div><div>CUSTOM</div><div class="featured">New Video Ads<br>MOnthly</div><div>17 Holiday<br>Themed video</div><div>4 Seasonal<br>Themed video</div><div>Daily 8 video for<br>Social Media</div></div>
    <div class="row body-row band"><div>COST PER VIDEO FORMAT</div><div>Starts @ $37/video</div><div class="featured">Starts @ $16/video</div><div>Starts @ $14/video</div><div>Starts @ $18/video</div><div>Starts @ $10/video</div></div>
    <div class="row body-row"><div>DELIVERY SPEED</div><div>24 HOURS</div><div class="featured">24 HOURS</div><div>3-5 DAYS</div><div>3-5 DAYS</div><div>PRIOR TO NEXT MONTH</div></div>
    <div class="row body-row band"><div>REVISIONS</div><div>UNLIMITED</div><div class="featured">UNLIMITED</div><div>UNLIMITED</div><div>UNLIMITED</div><div>UNLIMITED</div></div>
    <div class="row body-row"><div>FINAL FILE FORMATS</div><div>Mp4 FULL HD 1080P</div><div class="featured">Mp4 FULL HD 1080P</div><div>Mp4 FULL HD 1080P</div><div>Mp4 FULL HD 1080P</div><div>Mp4 FULL HD 1080P</div></div>
    <div class="row body-row band"><div>WIDE SCREEN VIDEO FORMAT</div><div>INCLUDED</div><div class="featured">INCLUDED</div><div>INCLUDED</div><div>INCLUDED</div><div>INCLUDED</div></div>
    <div class="row body-row"><div>LARGE SQUARE VIDEO FORMAT</div><div>INCLUDED</div><div class="featured">INCLUDED</div><div>INCLUDED</div><div>INCLUDED</div><div>INCLUDED</div></div>
    <div class="row body-row band"><div>VERTICAL VIDEO FORMAT</div><div>INCLUDED</div><div class="featured">INCLUDED</div><div>INCLUDED</div><div>INCLUDED</div><div>NOT INCLUDED</div></div>
    <div class="row body-row"><div>SOCIAL COVER VIDEO FORMAT</div><div>INCLUDED</div><div class="featured">INCLUDED</div><div>INCLUDED</div><div>INCLUDED</div><div>NOT INCLUDED</div></div>
    <div class="row body-row band"><div>HOLIDAY THEME VIDEO</div><div>OPTIONAL</div><div class="featured">INCLUDED</div><div>INCLUDED</div><div>NOT INCLUDED</div><div>INCLUDED</div></div>
    <div class="row body-row"><div>SEASONAL THEME VIDEO</div><div>OPTIONAL</div><div class="featured">INCLUDED</div><div>NOT INCLUDED</div><div>INCLUDED</div><div>NOT INCLUDED</div></div>
    <div class="row body-row band"><div>CONTENT DONE FOR YOU</div><div>INCLUDED</div><div class="featured">INCLUDED</div><div>INCLUDED</div><div>INCLUDED</div><div>INCLUDED</div></div>
    <div class="row body-row"><div>FULL BRANDING IN VIDEO</div><div>INCLUDED</div><div class="featured">INCLUDED</div><div>INCLUDED</div><div>INCLUDED</div><div>INCLUDED</div></div>
    <div class="row body-row band"><div>FULL COPYRIGHT OWNERSHIP</div><div>INCLUDED</div><div class="featured">INCLUDED</div><div>INCLUDED</div><div>INCLUDED</div><div>INCLUDED</div></div>
    <div class="row body-row"><div>FULL RESELLING RIGHTS</div><div>INCLUDED</div><div class="featured">INCLUDED</div><div>INCLUDED</div><div>INCLUDED</div><div>INCLUDED</div></div>
    <div class="row body-row band"><div>USE MY IMAGES</div><div>INCLUDED</div><div class="featured">INCLUDED</div><div>INCLUDED</div><div>INCLUDED</div><div>INCLUDED</div></div>
    <div class="row body-row"><div>USE MY VIDEO FOOTAGE</div><div>INCLUDED</div><div class="featured">INCLUDED</div><div>INCLUDED</div><div>INCLUDED</div><div>INCLUDED</div></div>
    <div class="row body-row band"><div>USE MY BACKGROUND MUSIC</div><div>INCLUDED</div><div class="featured">INCLUDED</div><div>INCLUDED</div><div>INCLUDED</div><div>INCLUDED</div></div>
    <div class="row body-row"><div>FULLY LICENSED BACKGROUND MUSIC</div><div>INCLUDED</div><div class="featured">INCLUDED</div><div>INCLUDED</div><div>INCLUDED</div><div>INCLUDED</div></div>
  </section>

  <div class="buy-strip">
    <div><span class="buy">BUY NOW</span></div>
    <div><span class="buy">BUY NOW</span></div>
    <div><span class="buy">BUY NOW</span></div>
  </div>

  <section class="calc">
    <div class="calc-grid spin-row">
      <div><span class="spinner">3<svg width="14" height="18" viewBox="0 0 14 18"><path d="M7 1 13 7H1z M7 17 1 11h12z" fill="#d9ecff"/></svg></span></div>
      <div class="featured"><span class="spinner">5<svg width="14" height="18" viewBox="0 0 14 18"><path d="M7 1 13 7H1z M7 17 1 11h12z" fill="#d9ecff"/></svg></span></div>
    </div>
    <div class="gap"></div>
    <div class="calc-grid sum band"><div><span>Total</span><span>$149</span></div><div class="featured"><span>Total</span><span>$99</span></div></div>
    <div class="calc-grid sum"><div><span>Discount</span><span>$29.80</span></div><div class="featured"><span>Discount</span><span>$19.80</span></div></div>
    <div class="calc-grid sum band"><div><span>Price Per Video</span><span>$119.20</span></div><div class="featured"><span>Price Per Video</span><span>$79.20</span></div></div>
    <div class="calc-grid sum grand"><div><span>Grand Total</span><span>$119.20</span></div><div class="featured"><span>Grand Total</span><span>$79.20</span></div></div>
    <div class="calc-grid">
      <div class="buy-bar"><span class="buy">BUY NOW</span></div>
      <div class="buy-bar"><span class="buy">BUY NOW</span></div>
    </div>
  </section>

  <footer class="footer">
    <div class="foot-brand brand"><div class="brand-name">VIMLO</div><div class="brand-tag">MARKETING VIDEOS MADE FOR YOU</div></div>
    <p class="foot-claim">CREATED BY A MARKETER FOR MARKETERS.</p>
    <div class="foot-col" style="left:777px">
      <h4>Quick Links</h4>
      <ul class="links"><li>How It Works</li><li>Term Of Service</li><li>Privacy Policy</li><li>Cookies Policy</li></ul>
    </div>
    <div class="foot-col" style="left:1032px">
      <h4>About Us</h4>
      <p class="about">With Vimlo, you simply let us know what you want to promote and we will have your video ad finished as soon as 24 hours!</p>
      <div class="socials" aria-label="Social links"><span></span><span></span><span></span><span></span><span></span></div>
    </div>
  </footer>

</div>
</body>
</html>
```